ARC VOLLEY Business Card Project

I'd like to request a business card design for the new company I've launched.
The name of the company is "ARC VOLLEY" an indoor unmanned tennis practice facility.
We would like to see designs that use our brand identity color in the logo I've attached.
We hope to get the design with modern, luxurious and elegant tone and manner.
We hope the logo should not be too big.

Business card must have elements as below:
- Logo (One of the logos I've attached)
- Name (In Korean Text) : 박 서 윤
- Title (In Korean Text) : 대표
- Phone Number : 010-8472-3916
- Email Address : seoyun.park@arcvolley-example.co.kr
- Website : www.arcvolley-example.co.kr
- Instagram : arcvolley
- Address (In Korean text) : 경기도 용인시 수지구 풍덕천로 456 미래타워 5층 501호, 502호

Target Market(s)

Tennis amateurs in 20 to 40s

Industry/Entity Type

Sports, Hobby

Contact Information for Business Card

- Logo (One of the logos I've attached) - Name (In Korean Text) : 박 서 윤 - Title (In Korean Text) : 대표 - Phone Number : 010-8472-3916 - Email Address : seoyun.park@arcvolley-example.co.kr - Website : www.arcvolley-example.co.kr - Instagram : arcvolley - Address (In Korean text) : 경기도 용인시 수지구 풍덕천로 456 미래타워 5층 501호, 502호

Font styles to use
Sans Serif

Requirements
Must have
• Double sided
Nice to have
• Logo with intaglio or relief embossing
Should not have
• Logo should not be too big.

```html
<!DOCTYPE html>
<html lang="ko">
<head>
<meta charset="utf-8">
<title>ARC VOLLEY Business Card</title>
<link rel="stylesheet" href="https://fonts.googleapis.com/css2?family=Cormorant+Garamond:wght@500;600&family=Noto+Sans+KR:wght@400;700&display=swap">
<style>
  :root {
    --bg: #e9e6e1;
    --gold-dark: #a9792c;
    --gold-mid: #d6a948;
    --gold-light: #f6d57c;
    --gold-text: #d9a93e;
    --green-deep: #0b2a17;
    --green: #163f24;
    --green-band: #1b4a2b;
    --ink-logo: #3d4a3a;
    --white: #f4f1ea;
  }
  * { margin: 0; padding: 0; box-sizing: border-box; }
  html, body { width: 1200px; height: 1200px; overflow: hidden; }
  body {
    background: var(--bg);
    position: relative;
    font-family: "Noto Sans KR", sans-serif;
  }
  .card {
    position: absolute;
    left: 240px;
    width: 720px;
    height: 410px;
    overflow: hidden;
    box-shadow: 0 10px 28px rgba(0,0,0,0.25);
  }
  .card--front { top: 180px; }
  .card--back { top: 630px; background: linear-gradient(90deg, var(--green-deep), var(--green) 60%, var(--green-band)); }

  /* front */
  .front__gold {
    position: absolute; inset: 0 0 103px 0;
    background: linear-gradient(100deg, var(--gold-dark) 0%, var(--gold-mid) 25%, var(--gold-light) 50%, var(--gold-mid) 75%, var(--gold-dark) 100%);
  }
  .front__texture {
    position: absolute; top: 0; right: 0; width: 330px; height: 410px;
    background: linear-gradient(135deg, rgba(255,230,150,0.15), rgba(90,60,20,0.18));
  }
  .front__band {
    position: absolute; left: 0; right: 0; bottom: 0; height: 103px;
    background: var(--green-band);
    display: flex; align-items: center; justify-content: center;
  }
  .front__url {
    font-family: "Cormorant Garamond", serif;
    font-size: 21px; letter-spacing: 2.5px; color: var(--white);
  }
  .brand {
    position: absolute; left: 0; right: 0; top: 80px;
    display: flex; flex-direction: column; align-items: center; gap: 14px;
  }
  .brand__mark { width: 84px; height: 84px; border-radius: 50%; background: var(--ink-logo); }
  .brand__name {
    font-family: "Cormorant Garamond", serif;
    font-weight: 600; font-size: 34px; letter-spacing: 1px; color: var(--ink-logo);
  }

  /* back */
  .back__texture {
    position: absolute; left: 0; top: 0; width: 390px; height: 410px;
    background: linear-gradient(135deg, #1f5a33 0%, #0a2614 45%, #154a29 75%, #06190d 100%);
    opacity: 0.85;
  }
  .profile {
    position: absolute; right: 58px; top: 44px; text-align: right;
  }
  .profile__name { font-size: 32px; font-weight: 700; color: var(--gold-text); letter-spacing: 3px; }
  .profile__title { font-size: 15px; font-weight: 700; color: var(--gold-text); margin-top: 2px; }
  .profile__rule {
    position: absolute; right: 58px; top: 130px; width: 150px; height: 2px; background: var(--gold-text);
  }
  .contacts {
    position: absolute; right: 58px; top: 160px;
    list-style: none; display: flex; flex-direction: column; gap: 16px; align-items: flex-end;
  }
  .contact {
    display: flex; align-items: center; gap: 14px;
    font-size: 16px; color: var(--gold-text); text-align: right; line-height: 1.3;
  }
  .contact__text--latin { font-family: "Cormorant Garamond", serif; font-weight: 600; font-size: 18px; letter-spacing: 0.4px; }
  .contact svg { width: 18px; height: 18px; flex: none; fill: var(--gold-text); }
</style>
</head>
<body>
  <section class="card card--front">
    <div class="front__gold"></div>
    <div class="front__texture" role="img" aria-label="Quilted diamond lattice pattern in gold tones"></div>
    <div class="brand">
      <div class="brand__mark"></div>
      <div class="brand__name">ARC VOLLEY</div>
    </div>
    <div class="front__band">
      <span class="front__url">www.arcvolley-example.co.kr</span>
    </div>
  </section>

  <section class="card card--back">
    <div class="back__texture" role="img" aria-label="Quilted diamond lattice pattern in deep green tones"></div>
    <div class="profile">
      <div class="profile__name">박서윤</div>
      <div class="profile__title">대표</div>
    </div>
    <div class="profile__rule"></div>
    <ul class="contacts">
      <li class="contact">
        <span class="contact__text--latin">SEOYUN.PARK@ARCVOLLEY-EXAMPLE.CO.KR</span>
        <svg viewBox="0 0 24 24" aria-hidden="true"><path d="M2 5h20v14H2z M4 7v1l8 5 8-5V7l-8 5z" fill-rule="evenodd"/></svg>
      </li>
      <li class="contact">
        <span class="contact__text--latin">010-8472-3916</span>
        <svg viewBox="0 0 24 24" aria-hidden="true"><path d="M6.6 10.8a15 15 0 0 0 6.6 6.6l2.2-2.2c.3-.3.7-.4 1-.2 1.1.4 2.3.6 3.6.6.6 0 1 .4 1 1V20c0 .6-.4 1-1 1C10.6 21 3 13.4 3 4c0-.6.4-1 1-1h3.5c.6 0 1 .4 1 1 0 1.3.2 2.5.6 3.6.1.3 0 .7-.2 1z"/></svg>
      </li>
      <li class="contact">
        <span class="contact__text--latin">ARCVOLLEY</span>
        <svg viewBox="0 0 24 24" aria-hidden="true"><rect x="3" y="3" width="18" height="18" rx="2" fill="none" stroke="#d9a93e" stroke-width="2.2"/></svg>
      </li>
      <li class="contact">
        <span class="contact__text--latin">WWW.ARCVOLLEY-EXAMPLE.CO.KR</span>
        <svg viewBox="0 0 24 24" aria-hidden="true"><g fill="none" stroke="#d9a93e" stroke-width="2"><circle cx="12" cy="12" r="9"/><ellipse cx="12" cy="12" rx="4" ry="9"/><path d="M3 12h18"/></g></svg>
      </li>
      <li class="contact">
        <span>경기도 용인시 수지구 풍덕천로<br>456 미래타워 5층 501호, 502호</span>
        <svg viewBox="0 0 24 24" aria-hidden="true"><path d="M12 2a7 7 0 0 0-7 7c0 5 7 13 7 13s7-8 7-13a7 7 0 0 0-7-7zm0 9.5A2.5 2.5 0 1 1 12 6.5a2.5 2.5 0 0 1 0 5z"/></svg>
      </li>
    </ul>
  </section>
</body>
</html>
```